New Website for novelty yarn producer

We need a new website for our company, Tarvek. We make highly tailored yarns for weavers worldwide. This year marks our 40th anniversary and we want to evolve our image and identity.

Our temporary website can be found at:
www.tarvekyarns.com

Our only concern in that throughout the website the protagonist must be our client, we make their creations possible and are highly adaptable both during the ideation process of the yarn as well as in the production. This is at the core of the way we do business and is summarised within the concept of FPM (Fluid Partner Method).

Industry/Entity Type

Textile

Number of Pages Required

1 page

Colors
9bcb3c

Requirements
Must have
• Fluid Partner Method (FPM) - can be found on or current website www.tarvekyarns.com

```html
<!DOCTYPE html>
<html lang="en">
<head>
<meta charset="utf-8">
<title>Tarvek Novelty Yarn Solutions</title>
<link rel="stylesheet" href="https://fonts.googleapis.com/css2?family=Open+Sans:wght@400;600;700&family=Montserrat:wght@600;700&family=Playfair+Display+SC:wght@400;700&family=Playfair+Display:wght@400&display=swap">
<style>
:root{
  --green:#9bcb3c;
  --black:#0a0a0a;
  --ink:#1c1c1c;
  --text:#666666;
  --grey-bg:#f7f7f7;
  --light-num:#e6e6e6;
  --line:#bdbdbd;
  --white:#ffffff;
}
*{margin:0;padding:0;box-sizing:border-box}
html,body{width:1200px;height:2403px;overflow:hidden;background:var(--white)}
body{position:relative;font-family:"Open Sans",Arial,sans-serif;color:var(--ink)}
.abs{position:absolute}

/* top bar */
.topbar{left:0;top:0;width:1200px;height:80px;background:var(--black);color:var(--white);font-size:12px}
.top-contact{top:31px;display:flex;align-items:center;gap:8px}
.brand{left:460px;top:0;width:280px;text-align:center}
.brand-name{font-family:"Playfair Display",serif;font-size:58px;line-height:78px;color:var(--white);letter-spacing:1px}

/* nav */
.nav{left:0;top:80px;width:1200px;height:45px;background:var(--white);border-bottom:1px solid #e5e5e5}
.nav a{position:absolute;top:14px;font-size:11px;color:var(--ink);text-decoration:none}
.nav a.active{border-bottom:2px solid var(--green);padding-bottom:9px}

/* hero */
.hero{left:0;top:125px;width:1200px;height:506px;background:linear-gradient(100deg,#3a2226 0%,#5c2734 30%,#4a3532 55%,#3b3330 75%,#6b5a3a 100%)}
.hero-shade{left:0;top:0;width:1200px;height:506px;background:rgba(0,0,0,.28)}
.badge{left:772px;top:70px;width:90px;height:90px;border:2px solid var(--white);border-radius:50%;text-align:center;color:var(--white)}
.badge b{display:block;font-family:"Playfair Display",serif;font-weight:400;font-size:34px;line-height:38px;margin-top:14px}
.badge span{font-family:"Playfair Display",serif;font-size:10px}
.hero-title{left:560px;top:198px;width:520px;text-align:center;font-family:"Playfair Display SC",serif;font-weight:400;font-size:31px;line-height:44px;white-space:nowrap;color:var(--white)}
.ribbon{left:601px;top:272px;width:432px;height:48px;background:var(--green);color:var(--white);font-family:"Montserrat",sans-serif;font-weight:700;font-size:24px;text-align:center;line-height:48px;box-shadow:0 3px 6px rgba(0,0,0,.35)}
.ribbon i{display:inline-block;width:14px;height:14px;border:2px solid var(--white);border-radius:50%;vertical-align:middle;margin:0 14px}
.hero-copy{left:600px;top:347px;width:440px;text-align:center;color:var(--white);font-size:14px;font-weight:600;line-height:22.5px;text-transform:uppercase}

/* section headings */
.heading{left:160px;width:880px;height:40px;display:flex;align-items:center;gap:10px}
.heading .rule{flex:1;border-top:2px dashed #555}
.heading .knot{flex:none;width:18px;height:18px;border:2px solid #333;border-radius:50%}
.heading h2{flex:none;font-family:"Playfair Display SC",serif;font-weight:400;font-size:27px;line-height:40px;white-space:nowrap;color:var(--ink);padding:0 6px}

/* flexible section */
.flex-photo{left:162px;top:774px;width:405px;height:245px;border:3px solid #f2f2f2;background:linear-gradient(135deg,#7ac7b7 0%,#3c7fb8 22%,#e8c43a 45%,#9bcb3c 60%,#c73a4a 78%,#e8e0d4 100%)}
.flex-copy{left:601px;top:790px;width:390px;font-size:11px;line-height:19.5px;color:var(--text)}
.flex-copy h3{font-size:12.5px;color:var(--green);font-weight:600;margin-bottom:2px}
.flex-copy h4{font-size:11.5px;color:var(--ink);font-weight:600;margin-bottom:2px}
.read-more{display:inline-block;margin-top:14px;font-family:"Montserrat",sans-serif;font-weight:700;font-size:11.5px;color:var(--ink)}

/* features */
.features{left:0;top:1100px;width:1200px;height:736px;background:var(--grey-bg)}
.card{top:178px}
.card .photo{height:305px}
.card .body{height:102px;border:2px dashed #c8e49a;border-top:none;background:var(--white);padding:10px 16px;position:relative}
.card h3{font-family:"Montserrat",sans-serif;font-weight:700;font-size:17px;color:var(--ink);margin-bottom:8px;white-space:nowrap}
.card p{font-size:11px;line-height:18px;color:var(--text);width:205px;max-height:36px;overflow:hidden}
.card .more{position:absolute;right:14px;bottom:10px;font-family:"Montserrat",sans-serif;font-weight:700;font-size:10.5px;color:var(--green)}
.card .btn{position:absolute;right:10px;top:46px;width:114px;height:30px;background:var(--green);color:var(--white);font-family:"Montserrat",sans-serif;font-weight:700;font-size:11px;line-height:30px;text-align:center;border-radius:3px}
.pager{top:638px;width:30px;height:30px;border:1px solid #ccc;border-radius:50%;background:var(--white)}
.pager svg{display:block;margin:8px auto}

/* numbers */
.numbers-intro{left:160px;top:1930px;width:220px;text-align:center}
.numbers-intro h3{font-family:"Montserrat",sans-serif;font-weight:700;font-size:19px;color:#333;padding-bottom:10px;border-bottom:3px solid #666;margin-top:30px}
.numbers-intro p{font-size:11.5px;line-height:16.5px;color:var(--text);margin-top:25px}
.numbers-intro a{display:block;margin-top:14px;font-family:"Montserrat",sans-serif;font-weight:700;font-size:10.5px;color:var(--ink);text-decoration:none}
.stat{top:1950px;width:220px;text-align:center}
.stat b{display:block;font-family:"Montserrat",sans-serif;font-weight:700;font-size:86px;line-height:95px;color:var(--light-num)}
.stat span{display:block;font-family:"Montserrat",sans-serif;font-weight:700;font-size:11.5px;color:#333;margin-top:12px}

/* newsletter */
.divider{left:30px;top:2215px;width:1170px;border-top:2px dotted var(--line)}
.news-label{left:227px;top:2250px;font-family:"Montserrat",sans-serif;font-weight:700;font-size:15px;color:var(--ink)}
.news-input{left:449px;top:2243px;width:344px;height:35px;border:1px solid #ddd;font-size:11px;color:#888;line-height:33px;padding-left:16px}
.news-btn{left:809px;top:2243px;width:96px;height:35px;background:var(--green);color:var(--white);font-family:"Montserrat",sans-serif;font-weight:700;font-size:12px;line-height:35px;text-align:center;border-radius:2px}

/* footer */
.footer{left:0;top:2310px;width:1200px;height:48px;background:var(--black)}
.footer-links{left:160px;top:16px;font-size:11px;color:#d8d8d8;word-spacing:2px}
.social{top:12px;width:24px;height:24px;border:1.5px solid var(--white);border-radius:50%}
.legal{top:2373px;font-size:11px;color:#333}
</style>
</head>
<body>

<header class="abs topbar">
  <div class="abs top-contact" style="left:160px">
    <svg width="16" height="12" viewBox="0 0 16 12"><rect x="1" y="1" width="14" height="10" fill="none" stroke="#fff" stroke-width="1.5"/><path d="M1 1l7 6 7-6" fill="none" stroke="#fff" stroke-width="1.5"/></svg>
    <span>info@tarvekyarnstudio.com</span>
  </div>
  <div class="abs brand">
    <div class="brand-name">TARVEK</div>
  </div>
  <div class="abs top-contact" style="left:950px">
    <svg width="18" height="14" viewBox="0 0 18 14"><path d="M1 5c0-3 16-3 16 0v2h-4V5H5v2H1z" fill="#fff"/><rect x="4" y="7" width="10" height="6" rx="1" fill="#fff"/></svg>
    <span>0574 20918</span>
  </div>
</header>

<nav class="abs nav">
  <a class="active" href="#" style="left:168px">Home</a>
  <a href="#" style="left:248px">About Us</a>
  <a href="#" style="left:343px">Fluid Partner Method</a>
  <a href="#" style="left:753px">Heritage</a>
  <a href="#" style="left:846px">Team</a>
  <a href="#" style="left:922px">Blogs</a>
  <a href="#" style="left:997px">Contact</a>
</nav>

<section class="abs hero" role="img" aria-label="Photograph of deep red yarn strung across a wooden weaving loom with colourful fabric behind">
  <div class="abs hero-shade"></div>
  <div class="abs badge"><b>40</b><span>Tarvek</span></div>
  <h1 class="abs hero-title">Tailored Weaving Solutions</h1>
  <div class="abs ribbon"><i></i>Make Since 40th Year<i></i></div>
  <p class="abs hero-copy">TNYS combines the experience of a team that has served the weaving industry for over 40 years, fully dedicated to the success of our clients</p>
</section>

<div class="abs heading" style="top:696px">
  <span class="rule"></span><span class="knot"></span>
  <h2>Flexible At The Core</h2>
  <span class="knot"></span><span class="rule"></span>
</div>

<div class="abs flex-photo" role="img" aria-label="Photograph of rolled woven fabrics in a diagonal rainbow of colours"></div>
<div class="abs flex-copy">
  <h3>TNYS Fluid Partner Method</h3>
  <h4>Your Tailored Clothes Experience :</h4>
  <p>We believe that the key to delivering a yarn that exceeds our client's expectation is to work together with weavers from step one, starting from the desired end product and working backwards. This allows us to develop the product that our weavers need, rather than having weavers adapt to the supplied raw materials.</p>
  <p>Our Fluid Partner Method consists achieving maximum flexibility both in development and production.</p>
  <span class="read-more">Read More</span>
</div>

<section class="abs features">
  <div class="abs heading" style="top:85px">
    <span class="rule"></span><span class="knot"></span>
    <h2>Tarvek Novelty Yarn Solution</h2>
    <span class="knot"></span><span class="rule"></span>
  </div>

  <article class="abs card" style="left:42px;width:395px">
    <div class="photo" role="img" aria-label="Photograph of stacked yellow and orange fabrics beside a tape measure" style="background:linear-gradient(160deg,#e9c06a,#e59a2a 55%,#c9782a)"></div>
    <div class="body">
      <h3>Production built around you</h3>
      <p>Versatility and flexibility both in development and production are key...</p>
      <span class="btn">FIND OUT MORE</span>
    </div>
  </article>
  <article class="abs card" style="left:460px;width:218px">
    <div class="photo" role="img" aria-label="Photograph of spinning machinery winding yarn" style="background:linear-gradient(160deg,#9a9a96,#5b5a56 60%,#3a3936)"></div>
    <div class="body">
      <h3>Experience</h3>
      <p style="width:150px">Over the years the company has gained...</p>
      <span class="more">MORE</span>
    </div>
  </article>
  <article class="abs card" style="left:700px;width:218px">
    <div class="photo" role="img" aria-label="Photograph of twisted yellow and purple yarn on dark cloth" style="background:linear-gradient(160deg,#3b3b40,#2a2a30 60%,#4a4438)"></div>
    <div class="body">
      <h3>Creativity</h3>
      <p style="width:150px">Our belief is that the key to our clients' success is a...</p>
      <span class="more">MORE</span>
    </div>
  </article>
  <article class="abs card" style="left:940px;width:218px">
    <div class="photo" role="img" aria-label="Black and white photograph of a workshop with yarn cones on a table" style="background:linear-gradient(160deg,#d8d8d8,#8a8a8a 60%,#4a4a4a)"></div>
    <div class="body">
      <h3>Professionality</h3>
      <p style="width:184px">We are a family business at the core. Our company is run with</p>
      <span class="more">MORE</span>
    </div>
  </article>

  <span class="abs pager" style="left:565px"><svg width="12" height="12" viewBox="0 0 12 12"><path d="M7 2L3 6l4 4" fill="none" stroke="#555" stroke-width="1.5"/></svg></span>
  <span class="abs pager" style="left:602px"><svg width="12" height="12" viewBox="0 0 12 12"><path d="M5 2l4 4-4 4" fill="none" stroke="#555" stroke-width="1.5"/></svg></span>
</section>

<div class="abs numbers-intro">
  <h3>TYS IN NUMBERS</h3>
  <p>Our team has decades of experience in providing yarn solutions to weavers around the world, assisting them in the creation of outstanding textiles.</p>
  <a href="#">Find Out More</a>
</div>
<div class="abs stat" style="left:462px"><b>40</b><span>YEARS IN BUSNESS</span></div>
<div class="abs stat" style="left:643px"><b>8</b><span>BRANDS</span></div>
<div class="abs stat" style="left:816px"><b>2</b><span>MILLION KILOGRAMS/ YR</span></div>

<div class="abs divider"></div>
<div class="abs news-label">Subscribe our Newsletter</div>
<div class="abs news-input">Enter your email id</div>
<div class="abs news-btn">SIGN UP</div>

<footer class="abs footer">
  <div class="abs footer-links">Email &nbsp;/ &nbsp;Home &nbsp;/ &nbsp;Products &nbsp;/ &nbsp;Articles &nbsp;/ &nbsp;FAQ &nbsp;/ &nbsp;Contact Us</div>
  <span class="abs social" style="left:920px"></span>
  <span class="abs social" style="left:952px"></span>
  <span class="abs social" style="left:984px"></span>
  <span class="abs social" style="left:1015px"></span>
</footer>
<div class="abs legal" style="left:160px">© Copyright 2018 Tarvek Novelty Yarn Solution, Italy. All Rights Reserved</div>
<div class="abs legal" style="left:908px">Privacy Policy &nbsp;/ &nbsp;Terms of Service</div>

</body>
</html>
```